Book Title: WHEN RIVERS LISTEN

I want to test how good this title is and what is the best cover design for my book

Target Market(s)

Sales people, Entrepreneurs, Public Speakers, Leaders in Business

Font styles to use
Sans Serif

Colors

Designer to choose colors to be used in the design.

Requirements
Must have
• Powerful positive energy emanating from an eagle
Nice to have
• Show an eagle clawing a prey
Should not have
• No negative energies

```html
<!DOCTYPE html>
<html lang="en">
<head>
<meta charset="utf-8">
<title>When Rivers Listen — Book Cover</title>
<link rel="stylesheet" href="https://fonts.googleapis.com/css2?family=Playfair+Display:wght@400&display=swap">
<style>
  :root {
    --backdrop: #eef1f4;
    --cover: #ffffff;
    --ink: #3d3d3f;
    --amber: #f5a623;
    --gold: #f1d46e;
    --tangerine: #f28c28;
    --eagle-dark: #2f2f31;
    --eagle-mid: #5c5c60;
  }
  * { box-sizing: border-box; margin: 0; padding: 0; }
  html, body {
    width: 1200px;
    height: 880px;
    overflow: hidden;
    background: var(--backdrop);
  }
  .stage {
    width: 1200px;
    height: 880px;
    display: flex;
    align-items: center;
    justify-content: center;
  }
  .book-cover {
    position: relative;
    width: 560px;
    height: 800px;
    background: var(--cover);
    box-shadow: 0 10px 30px rgba(0, 0, 0, 0.12);
    overflow: hidden;
  }
  .eagle-art {
    position: absolute;
    top: 96px;
    left: 60px;
    width: 440px;
    height: 210px;
    border-radius: 60% 60% 45% 45% / 70% 70% 30% 30%;
    background:
      radial-gradient(ellipse 22% 18% at 50% 82%, var(--amber) 0%, rgba(245,166,35,0) 100%),
      radial-gradient(ellipse at 50% 60%, var(--eagle-mid) 0%, var(--eagle-dark) 75%);
  }
  .title {
    position: absolute;
    inset: 0;
    font-family: "Playfair Display", "Times New Roman", serif;
    font-weight: 400;
    pointer-events: none;
  }
  .title-line {
    position: absolute;
    display: flex;
    font-size: 92px;
    line-height: 1;
    letter-spacing: -3px;
    transform: scaleY(1.85);
    transform-origin: top left;
    white-space: nowrap;
  }
  .title-line span { display: block; }
  .line-when   { top: 292px; left: 214px; }
  .line-rivers { top: 430px; left: 78px; }
  .line-listen { top: 568px; left: 140px; }
  .title-line .drop { transform: translateY(10px); }
  .title-line .lift { transform: translateY(-10px); }
  .c-ink { color: var(--ink); }
  .c-amber { color: var(--amber); }
  .c-gold { color: var(--gold); }
  .c-tangerine { color: var(--tangerine); }
</style>
</head>
<body>
  <main class="stage">
    <section class="book-cover">
      <div class="eagle-art" role="img" aria-label="Illustration of a dark eagle with spread wings swooping down, golden talons outstretched"></div>
      <h1 class="title" aria-label="When Rivers Listen">
        <span class="title-line line-when" aria-hidden="true"><span class="c-gold">W</span><span class="c-gold lift">H</span><span class="c-tangerine">E</span><span class="c-amber drop">N</span></span>
        <span class="title-line line-rivers" aria-hidden="true"><span class="c-ink lift">R</span><span class="c-ink">I</span><span class="c-amber drop">V</span><span class="c-tangerine">E</span><span class="c-ink lift">R</span><span class="c-tangerine">S</span></span>
        <span class="title-line line-listen" aria-hidden="true"><span class="c-gold">L</span><span class="c-gold drop">I</span><span class="c-amber">S</span><span class="c-ink lift">T</span><span class="c-ink">E</span><span class="c-gold drop">N</span></span>
      </h1>
    </section>
  </main>
</body>
</html>
```